Improving a camping website homepage header*

My client is very happy with his new website and its new functionalities. However, he's not very happy about the homepage design. Specifically, the header(this includes the menu, large header image and two columns beneath that). You can find the website here: http://lnkvo.example/siteTentra .

He forwarded me several other websites he likes. Which can be found in the attachments. I also included several pictures of the camping.

I'm looking for a design that will improve the header of the homepage with room for other global style chances. The logo cannot be changed.

Attachments
1) His old website homepage
2) Website mockup he liked.
3) Another website mockup he liked.

Other images can be found on the new website http://lnkvo.example/siteTentra or his old website http://lnkvo.example/formerSiteTentra.

Can you help us?
Updates

Hello guys. Here's a bit more information - Language used on the website is dutch. - The two columns left/right are supposed to link to Hire/Buy chalets. The client indicated that he finds these links important, but doesn't like the current design. I think this is partially the case because he doesn't like the icons. I'm looking forward to your designs!

Target Market(s)

30-50 year old wealthy people that want to purchase or rent cabins in the Netherlands.

Number of Pages Required

1 page

Colors

Designer to choose colors to be used in the design.

Requirements
Must have
• Improved header
Nice to have
• Global style changes
Should not have
• Logo changes

```html
<!DOCTYPE html>
<html lang="nl">
<head>
<meta charset="utf-8">
<title>Parc Veldenhove – Home</title>
<link href="https://fonts.googleapis.com/css2?family=Montserrat:wght@400;500;600;700&display=swap" rel="stylesheet">
<style>
:root{
  --green:#7d9f1e;
  --green-dark:#6a8a15;
  --orange:#e8862a;
  --blue:#458bcf;
  --blue-dark:#3a7dc0;
  --text:#333;
  --muted:#bbb;
  --line:#e6e6e6;
  --bg:#fff;
}
*{margin:0;padding:0;box-sizing:border-box}
html,body{width:870px;height:1200px;overflow:hidden;background:var(--bg);font-family:'Montserrat',sans-serif;color:var(--text)}
.page{position:relative;width:870px;height:1200px}
.topbar{position:absolute;left:0;top:0;width:870px;height:28px;background:var(--green);color:#fff;font-size:9px;font-weight:700}
.topbar .phone{position:absolute;left:118px;top:9px;display:flex;align-items:center;gap:6px}
.topbar .login{position:absolute;left:622px;top:9px}
.topbar .divider{position:absolute;left:678px;top:4px;width:2px;height:20px;background:#fff}
.topbar .social{position:absolute;left:701px;top:6px;display:flex;gap:3px}
.topbar .social span{width:16px;height:16px;border-radius:50%;background:#fff;display:block}
.nav{position:absolute;left:0;top:28px;width:870px;height:56px;background:#fff}
.brand{position:absolute;left:116px;top:14px;display:flex;align-items:center;gap:6px}
.brand .dot{width:14px;height:14px;border-radius:50%;background:var(--green)}
.brand .name{font-size:11px;font-weight:600;color:var(--green)}
.menu{position:absolute;right:116px;top:25px;display:flex;gap:11px;font-size:9px;font-weight:500;list-style:none}
.menu .active{color:var(--orange);font-weight:700}
.hero{position:absolute;left:0;top:84px;width:870px;height:405px;background:linear-gradient(180deg,#c9cfcf 0%,#9fb28a 8%,#5e7c45 25%,#6d7d5b 45%,#5a6f4d 58%,#7f9890 65%,#6e8c86 100%)}
.feature{position:absolute;top:522px}
.feature .icon-box{position:absolute;left:0;top:0;width:109px;height:108px;background:#fff;box-shadow:0 2px 12px rgba(0,0,0,.08);display:flex;align-items:center;justify-content:center}
.feature h2{position:absolute;left:134px;top:-2px;font-size:13px;line-height:16px;font-weight:700;color:var(--orange);white-space:nowrap}
.feature p{position:absolute;left:134px;top:26px;width:130px;font-size:8.4px;line-height:10.9px;color:#333}
.band{position:absolute;left:0;top:661px;width:870px;height:151px;background:var(--blue);display:flex;align-items:center;justify-content:center}
.band h2{color:#fff;font-size:16px;font-weight:600}
.card{position:absolute;top:865px;width:204px;height:271px;background:#fff;box-shadow:0 2px 12px rgba(0,0,0,.07)}
.card .head{height:49px;position:relative}
.card h3{position:absolute;left:14px;top:17px;font-size:12.5px;line-height:16px;font-weight:700;color:var(--orange)}
.btn{position:absolute;width:68px;height:27px;color:#fff;font-size:8.5px;display:flex;align-items:center;justify-content:center}
.btn.blue{background:var(--blue);left:118px;top:11px}
.btn.green{background:var(--green);left:118px;top:187px}
.card .photo{width:204px;height:128px;background:linear-gradient(180deg,#c6d2dc 0%,#9aa59a 35%,#c9cac4 50%,#6d7d4f 75%,#4d7a2c 100%)}
.card .photo.alt{background:linear-gradient(180deg,#a8c07d 0%,#7d9b55 35%,#e4e2d8 55%,#5f8d2e 78%,#3f6a20 100%)}
.specs{position:absolute;left:16px;top:181px;list-style:none;font-size:8.5px}
.specs li{display:flex;align-items:center;gap:8px;height:20px}
.price{position:absolute;right:18px;top:224px;font-size:8.5px;line-height:12px;color:var(--orange)}
.card .foot{position:absolute;left:0;top:241px;width:204px;height:30px;border-top:2px solid var(--line)}
.avatar{position:absolute;left:18px;top:7px;width:17px;height:17px;border-radius:50%;background:#8a9a80}
.author{position:absolute;left:42px;top:10px;font-size:8.5px}
.actions{position:absolute;right:22px;top:8px;display:flex;gap:5px}
.actions span{width:16px;height:15px;border:1px solid #eee;display:flex;align-items:center;justify-content:center}
</style>
</head>
<body>
<div class="page">
  <header>
    <div class="topbar">
      <div class="phone">
        <svg width="8" height="8" viewBox="0 0 10 10"><path d="M2 0.5 L4 2.5 L3 4 Q4.5 6 6 7 L7.5 6 L9.5 8 L8 9.5 Q3 9 0.5 2 Z" fill="#fff"/></svg>
        0300 - 12 34 56
      </div>
      <div class="login">Inloggen</div>
      <div class="divider"></div>
      <div class="social"><span></span><span></span><span></span></div>
    </div>
    <nav class="nav">
      <div class="brand"><span class="dot"></span><span class="name">Parc Veldenhove</span></div>
      <ul class="menu">
        <li class="active">Home</li><li>Het Park</li><li>Financiering</li><li>Chalets</li><li>Aanbiedingen</li><li>Faciliteiten</li><li>Contact</li>
      </ul>
    </nav>
  </header>

  <div class="hero" role="img" aria-label="Luchtfoto van het vakantiepark met chalets tussen bomen aan een meer"></div>

  <section class="feature" style="left:116px">
    <div class="icon-box">
      <svg width="58" height="36" viewBox="0 0 58 36">
        <path d="M2 16 L22 2 L40 2 L56 16 Z" fill="var(--green)"/>
        <rect x="5" y="16" width="48" height="18" fill="var(--green)"/>
        <rect x="9" y="20" width="10" height="9" fill="#fff"/>
        <rect x="24" y="20" width="6" height="14" fill="#fff"/>
        <rect x="37" y="20" width="11" height="9" fill="#fff"/>
      </svg>
    </div>
    <h2>Chalet huren</h2>
    <p>Lorem ipsum dolor sit amet, consectetur adipiscing elit. Aenean euismod bibendum laoreet. Proin gravida dolor sit amet lacus accumsan et viverra justo commodo.</p>
  </section>

  <section class="feature" style="left:442px">
    <div class="icon-box">
      <svg width="64" height="40" viewBox="0 0 64 40">
        <g fill="var(--green)">
          <path d="M2 14 L22 2 L62 22 L42 34 Z"/>
          <path d="M2 18 L42 38 L62 26 L62 28 L42 40 L2 20 Z"/>
        </g>
        <ellipse cx="32" cy="18" rx="8" ry="4.5" fill="#fff"/>
      </svg>
    </div>
    <h2>Chalet kopen</h2>
    <p>Lorem ipsum dolor sit amet, consectetur adipiscing elit. Aenean euismod bibendum laoreet. Proin gravida dolor sit amet lacus accumsan et viverra justo commodo.</p>
  </section>

  <section class="band">
    <h2>UW eigen droomhuis binnen handbereik</h2>
  </section>

  <article class="card" style="left:116px">
    <div class="head"><h3>Kavel 190</h3><span class="btn blue">Huren</span></div>
    <div class="photo" role="img" aria-label="Foto van het chalet op kavel 190 met tuin"></div>
    <ul class="specs">
      <li><svg width="14" height="8" viewBox="0 0 14 8"><path d="M1 0V8M1 5H13V8M4 3H12V5" stroke="var(--orange)" fill="none"/></svg>1 bedroom</li>
      <li><svg width="14" height="10" viewBox="0 0 14 10"><path d="M1 4H13L11 9H3Z" fill="none" stroke="var(--orange)"/><path d="M3 4V1H6" stroke="var(--orange)" fill="none"/></svg>3 bathrooms</li>
      <li><svg width="14" height="10" viewBox="0 0 14 10"><path d="M1 0V9H13Z" fill="none" stroke="var(--orange)"/></svg>105 m²</li>
    </ul>
    <span class="btn green">lees meer</span>
    <span class="price">€ 350 per maand</span>
    <div class="foot"><span class="avatar"></span><span class="author">admin</span>
      <div class="actions"><span><svg width="7" height="7"><circle cx="1.5" cy="3.5" r="1.2" fill="#ccc"/><circle cx="5.5" cy="1.5" r="1.2" fill="#ccc"/><circle cx="5.5" cy="5.5" r="1.2" fill="#ccc"/></svg></span><span><svg width="8" height="7" viewBox="0 0 8 7"><path d="M4 7 L0.5 3 A1.8 1.8 0 0 1 4 1.5 A1.8 1.8 0 0 1 7.5 3 Z" fill="#ccc"/></svg></span><span><svg width="7" height="7"><path d="M3.5 0V7M0 3.5H7" stroke="#ccc"/></svg></span></div>
    </div>
  </article>

  <article class="card" style="left:332px">
    <div class="head"><h3>Kavel 233</h3><span class="btn blue">Kopen</span></div>
    <div class="photo alt" role="img" aria-label="Foto van het chalet op kavel 233 aan het water"></div>
    <ul class="specs">
      <li><svg width="14" height="8" viewBox="0 0 14 8"><path d="M1 0V8M1 5H13V8M4 3H12V5" stroke="var(--orange)" fill="none"/></svg>1 bedroom</li>
      <li><svg width="14" height="10" viewBox="0 0 14 10"><path d="M1 4H13L11 9H3Z" fill="none" stroke="var(--orange)"/><path d="M3 4V1H6" stroke="var(--orange)" fill="none"/></svg>1 bathrooms</li>
      <li><svg width="14" height="10" viewBox="0 0 14 10"><path d="M1 0V9H13Z" fill="none" stroke="var(--orange)"/></svg>130 m²</li>
    </ul>
    <span class="btn green">lees meer</span>
    <span class="price">€ 205.000</span>
    <div class="foot"><span class="avatar"></span><span class="author">admin</span>
      <div class="actions"><span><svg width="7" height="7"><circle cx="1.5" cy="3.5" r="1.2" fill="#ccc"/><circle cx="5.5" cy="1.5" r="1.2" fill="#ccc"/><circle cx="5.5" cy="5.5" r="1.2" fill="#ccc"/></svg></span><span><svg width="8" height="7" viewBox="0 0 8 7"><path d="M4 7 L0.5 3 A1.8 1.8 0 0 1 4 1.5 A1.8 1.8 0 0 1 7.5 3 Z" fill="#ccc"/></svg></span><span><svg width="7" height="7"><path d="M3.5 0V7M0 3.5H7" stroke="#ccc"/></svg></span></div>
    </div>
  </article>

  <article class="card" style="left:550px">
    <div class="head"><h3>Kavel 236</h3><span class="btn blue">Kopen</span></div>
    <div class="photo" role="img" aria-label="Foto van het chalet op kavel 236 met tuin"></div>
    <ul class="specs">
      <li><svg width="14" height="8" viewBox="0 0 14 8"><path d="M1 0V8M1 5H13V8M4 3H12V5" stroke="var(--orange)" fill="none"/></svg>3 bedrooms</li>
      <li><svg width="14" height="10" viewBox="0 0 14 10"><path d="M1 4H13L11 9H3Z" fill="none" stroke="var(--orange)"/><path d="M3 4V1H6" stroke="var(--orange)" fill="none"/></svg>2 bathrooms</li>
      <li><svg width="14" height="10" viewBox="0 0 14 10"><path d="M1 0V9H13Z" fill="none" stroke="var(--orange)"/></svg>100 m²</li>
    </ul>
    <span class="btn green">lees meer</span>
    <span class="price">€ 195.000</span>
    <div class="foot"><span class="avatar"></span><span class="author">admin</span>
      <div class="actions"><span><svg width="7" height="7"><circle cx="1.5" cy="3.5" r="1.2" fill="#ccc"/><circle cx="5.5" cy="1.5" r="1.2" fill="#ccc"/><circle cx="5.5" cy="5.5" r="1.2" fill="#ccc"/></svg></span><span><svg width="8" height="7" viewBox="0 0 8 7"><path d="M4 7 L0.5 3 A1.8 1.8 0 0 1 4 1.5 A1.8 1.8 0 0 1 7.5 3 Z" fill="#ccc"/></svg></span><span><svg width="7" height="7"><path d="M3.5 0V7M0 3.5H7" stroke="#ccc"/></svg></span></div>
    </div>
  </article>
</div>
</body>
</html>
```